WordPress Direct-Booking Website for Bend, Oregon Vacation Rental — $750 Budget
Project Overview

We are looking for a talented WordPress designer/developer to create a clean, professional and inviting direct-booking website for Cedar Lantern Retreat, an established short-term vacation rental in Bend, Oregon.

The property is currently successfully listed on Staynest and Lodgr. Our Staynest property has approximately a 4.98-star rating with more than 200 reviews, is an Staynest Guest Pick, and ranks among the Top 1% of eligible homes.

Project Budget: $750

We will select the designer based on the quality of the initial concept, understanding of the property, proposed booking solution and ability to deliver a completed and functioning WordPress website.

Existing Staynest Listing

Please use our current Staynest listing as the primary reference for photographs, property details, amenities and design inspiration:

https://www.staynest.example/rooms/48170356

Original high-resolution photographs and additional property information will be provided to the selected designer.

Design Direction

We want the website to feel:

Upscale but comfortable
Warm and welcoming
Clean and uncluttered
Pacific Northwest / Central Oregon
Professional rather than corporate
Highly visual with large property photographs
Easy to navigate
Excellent on phones, tablets and desktop computers

We welcome creativity and want designers to show us their vision for the property rather than simply copying our Staynest listing.

The website should immediately communicate that Cedar Lantern Retreat is a highly rated vacation rental in an excellent Bend location.

Key Property Features
3 bedrooms
2 bathrooms
Sleeps up to 6 guests
Pet friendly
Approximately a 5-minute walk to Bend's Tanager Quarter
Near restaurants, shopping and Brightwater Lawn Pavilion
Private fenced backyard
Covered outdoor area
Off-street driveway parking
Fireplace
Well-equipped kitchen
Staynest Premier Host
Staynest Guest Pick
Top 1% of eligible Staynest homes
Approximately 4.98 stars with 200+ guest reviews

Our location, guest reviews, cleanliness, comfort, backyard, pet-friendly accommodations and walkability should be major selling points throughout the website.

Website Structure

We anticipate approximately 6–7 pages:

Home

Large hero photograph with a strong opening message and prominent BOOK DIRECT and CHECK AVAILABILITY buttons.

The home page should quickly communicate:

CEDAR LANTERN RETREAT — BEND, OREGON

3 Bedrooms | 2 Baths | Sleeps 6 | Pet Friendly | Walk to Tanager

Our exceptional guest rating and Staynest history should also be prominently featured.

The House

Bedrooms, bathrooms, kitchen, living areas, backyard and major amenities.

Photo Gallery

Large, attractive and fast-loading photographs with an easy-to-use mobile gallery.

Location / Explore Bend

Tanager Quarter, Brightwater Lawn Pavilion, Kettleback River, restaurants, breweries, shopping, downtown Bend and nearby outdoor recreation.

Guest Reviews

Selected guest reviews and prominent presentation of our strong Staynest reputation.

Availability & Book Direct

A simple and professional direct-booking experience.

Contact / FAQ

Contact information plus common questions regarding pets, parking, check-in/check-out, cancellations and other policies.

IMPORTANT — Direct Booking & Credit Card Requirements

We want guests to be able to book directly through the website without having to contact us first.

The website should use a proven WordPress vacation-rental booking plugin or system rather than a custom-built reservation/payment system.

Guests should be able to:

Select arrival and departure dates
See available dates
Enter number of guests
See nightly charges
See cleaning fees
See applicable lodging taxes and other charges
See the complete reservation total before paying
Enter guest/contact information
Pay securely by credit or debit card
Receive an automatic reservation confirmation

Paywell is our preferred credit-card processor.

Credit-card information must be processed securely through Paywell or another established payment processor. Credit-card information should NOT be stored directly on our WordPress website.

Staynest & Lodgr Calendar Synchronization

This is very important.

The direct-booking calendar must synchronize with our existing Staynest and Lodgr calendars to reduce the possibility of double bookings.

For this single-property website, we prefer a simple solution using Staynest/Lodgr calendar or iCal synchronization rather than an expensive monthly channel-management service, if practical.

The designer should clearly identify the booking plugin/system they propose using.

IMPORTANT — Tell Us Your Proposed Booking Solution

As part of your submission, please tell us:

Which WordPress booking plugin/system you recommend.
Whether it synchronizes availability with Staynest and Lodgr.
Whether it integrates directly with Paywell.
The initial cost of the plugin/software.
Any annual or monthly fees.
Whether any additional paid software or services will be required.

We strongly prefer a solution with little or no ongoing monthly software expense.

We do not want to select a designer and later discover that the proposed booking system requires an expensive monthly subscription.

WordPress & Technical Requirements

The completed project should include:

Fully functioning WordPress website
Responsive desktop/tablet/mobile design
Fast-loading pages
Optimized photographs
SSL/HTTPS compatibility
Direct-booking functionality
Paywell payment integration
Staynest calendar synchronization
Lodgr calendar synchronization
Automatic booking confirmations
Cleaning fee and lodging-tax calculations
Contact form
Wayfind Maps/location integration
Basic spam/security protection
Wayfind Metrics capability
Basic SEO setup
Search-engine submission capability
Easy owner editing of text, rates and photographs
Search Engine Optimization

The website should be structured for Wayfind and other search engines.

Important search themes include:

Bend Oregon vacation rental
Bend Oregon vacation home
Tanager Quarter vacation rental
Vacation rental near Tanager Bend
Bend Oregon pet-friendly vacation rental
Bend vacation rental near Brightwater Lawn Pavilion
Bend Oregon direct booking vacation rental

We are not expecting an extensive ongoing SEO campaign for the $750 project. We do expect proper page titles, descriptions, headings, image optimization and a good technical foundation for future SEO.

Ownership

Upon completion and final payment:

We own the completed WordPress website.
We receive full WordPress administrator access.
We control the domain and hosting accounts.
We own all custom design files created for the project.
All necessary login credentials are provided to us.
The website can be moved to another WordPress hosting provider in the future.
There should be no proprietary dependency on the developer after completion.
What We Want From Contestants

Please review our Staynest listing before submitting your concept.

We are particularly interested in seeing an initial homepage concept showing how you would present:

Cedar Lantern Retreat
The Bend / Tanager location
Our photography
Our exceptional guest reviews and ratings
The Book Direct message
The availability/booking call-to-action

We will provide feedback on the concepts we like and work with the selected designer to refine and complete the website.

Our Goal

Our objective is straightforward:

Create a beautiful, trustworthy and easy-to-use website that encourages guests to book Cedar Lantern Retreat directly with us.

The website will complement—not replace—our existing Staynest and Lodgr listings.

We want repeat guests and new customers to have an easy way to find the property, check availability and book directly while receiving the same professional experience they expect from a major vacation-rental platform.

Target Market(s)

Consumers looking to to travel to Mexico for vacation. Family or couples

Industry/Entity Type

Short term vacation rental industry

Coding

Coded - Design and coding required

Number of Pages Required

5+ page

Requirements
Must have
• Capabilities to accept credit card payments and link to other rental property sites calendars such as LODGR and Staynets
Nice to have
• Option for best plugins for property rental

```html
<!DOCTYPE html>
<html lang="en">
<head>
<meta charset="utf-8">
<title>Cedar Lantern Retreat — Bend, Oregon</title>
<link rel="stylesheet" href="https://fonts.googleapis.com/css2?family=Montserrat:wght@400;500;600;700;800&display=swap">
<style>
:root{
  --red:#c0272d;
  --red-dark:#a81f25;
  --ink:#1d1d1f;
  --text:#2b2b2b;
  --muted:#555;
  --blush:#fcf1f1;
  --blush-2:#f9e6e6;
  --grey:#f5f5f5;
  --white:#fff;
  --night:#232022;
}
*{box-sizing:border-box;margin:0;padding:0}
html,body{width:1200px;height:3333px;overflow:hidden}
body{font-family:"Montserrat",sans-serif;color:var(--text);background:var(--white);position:relative}
section,header,footer{position:absolute;left:0;width:1200px;overflow:hidden}
.abs{position:absolute}
.ph{position:absolute;border-radius:2px}

/* hero */
.hero{top:0;height:411px;background:linear-gradient(180deg,#231b15 0%,#4a3526 40%,#6a4b32 70%,#3a2a1f 100%)}
.hero-shade{position:absolute;inset:0;background:linear-gradient(90deg,rgba(10,8,6,.75) 0%,rgba(10,8,6,.35) 55%,rgba(10,8,6,.15) 100%)}
.logo{font-weight:700;color:var(--white);letter-spacing:.06em;font-size:15px}
.nav{top:41px;left:287px;display:flex;gap:12px;font-size:11.5px;color:#f0e8e0}
.pill{position:absolute;height:26px;border-radius:13px;font-size:11.5px;font-weight:500;display:flex;align-items:center;justify-content:center}
.pill.light{background:var(--white);color:var(--ink)}
.pill.red{background:var(--red);color:var(--white)}
.hero-title{top:160px;left:115px;font-size:42px;font-weight:700;color:var(--white);letter-spacing:.01em}
.hero-sub{top:206px;left:117px;font-size:12.5px;color:#e8ded6}
.facts{top:242px;left:119px;display:flex;gap:20px;font-size:10.5px;color:#f0e8e0}
.facts span::before{content:"";display:inline-block;width:5px;height:5px;border-radius:50%;background:#fff;margin-right:9px;vertical-align:middle}
.hero-rule{top:375px;left:0;width:1200px;height:1px;background:rgba(255,255,255,.25)}
.stats{top:386px;left:118px;display:flex;gap:18px;font-size:11px;color:#f0e8e0;align-items:center}
.stars{color:#f4b400;letter-spacing:1px}
.stats .dot{width:5px;height:5px;border-radius:50%;background:#fff}

/* intro */
.intro{top:411px;height:313px;background:var(--white)}
.intro h2{top:64px;left:640px;width:430px;font-size:20.5px;font-weight:600;line-height:1.08;color:var(--ink)}
.intro p{top:164px;left:642px;width:420px;font-size:11px;line-height:1.38;color:var(--text)}
.link{font-size:11.5px;font-weight:600;color:var(--red);text-decoration:underline}

/* rooms */
.rooms{top:724px;height:485px;background:var(--blush)}
.rooms h2{top:38px;left:119px;font-size:22px;font-weight:700;color:var(--ink)}
.rooms .lede{top:67px;left:119px;width:850px;font-size:12px;line-height:1.3;color:var(--text)}
.card{position:absolute;overflow:hidden}
.card.w{background:var(--white)}
.card.p{background:var(--blush-2)}
.card h3{position:absolute;left:14px;top:74px;font-size:14.5px;font-weight:600;color:var(--red)}
.card p{position:absolute;left:16px;top:97px;width:300px;font-size:10.5px;line-height:1.28;color:var(--text)}
.card svg.icon{position:absolute;top:14px;right:24px}
.card .arc{position:absolute;right:-38px;bottom:-74px;width:140px;height:140px;border-radius:50%;border:22px solid var(--red)}

/* gallery */
.gallery{top:1209px;height:515px;background:var(--white)}
.ghost{top:4px;left:-10px;font-size:102px;font-weight:800;color:#f3f3f3;white-space:nowrap;letter-spacing:.02em}
.gallery h2{top:36px;left:117px;font-size:22px;font-weight:700;color:var(--ink)}
.gallery .link{top:468px;left:530px;font-size:11px;letter-spacing:.04em}

/* reviews */
.reviews{top:1724px;height:419px;background:var(--grey)}
.reviews h2{top:38px;left:121px;font-size:22px;font-weight:700;color:var(--ink)}
.reviews h2 em{font-style:normal;color:var(--red);font-size:34px;font-weight:800}
.score{top:101px;left:115px;font-size:66px;font-weight:800;color:var(--red);letter-spacing:-.02em;line-height:1}
.score-stars{top:163px;left:183px;font-size:10px;color:var(--red);letter-spacing:1px}
.score-note{top:178px;left:122px;font-size:11.5px;color:var(--text)}
.metric{position:absolute;width:196px;font-size:11px;color:var(--text);border-bottom:2px solid var(--red);padding-bottom:9px}
.metric b{color:var(--red);font-weight:600}
.chip{position:absolute;top:228px;height:28px;border:1px solid #ddd;border-radius:14px;background:var(--white);font-size:11px;display:flex;align-items:center;justify-content:center}
.chip b{color:var(--red);font-weight:600;margin-left:3px}
.quote{position:absolute;font-size:12.5px;line-height:1.3;color:var(--text)}
.quote cite{display:block;font-style:normal;font-size:11px;color:var(--red);margin-top:18px}
.quote-card{position:absolute;top:289px;left:437px;width:322px;height:104px;background:var(--white)}

/* book direct */
.direct{top:2143px;height:404px;background:linear-gradient(135deg,#7a6a5c 0%,#a89584 40%,#c9b8a5 70%,#8a7563 100%)}
.direct-card{top:55px;left:540px;width:510px;height:272px;background:var(--red);border-radius:16px;overflow:hidden;color:var(--white)}
.direct-card h2{position:absolute;top:20px;left:22px;font-size:24.5px;font-weight:700;line-height:1.05}
.direct-card .lede{position:absolute;top:86px;left:26px;width:400px;font-size:11px;line-height:1.25}
.step{position:absolute;left:28px;display:flex;gap:12px;align-items:center;font-size:16.5px;font-weight:600}
.direct-card .btn{position:absolute;left:33px;top:227px;width:183px;height:29px;border-radius:15px;background:var(--white);color:var(--ink);font-size:13.5px;font-weight:700;display:flex;align-items:center;justify-content:center}
.direct-card .arc{position:absolute;right:-70px;bottom:-100px;width:200px;height:200px;border-radius:50%;border:28px solid var(--white)}

/* faq */
.faq{top:2547px;height:256px;background:var(--white)}
.faq h2{top:30px;left:121px;font-size:34px;font-weight:700;color:var(--ink)}
.qa{position:absolute;left:125px;width:452px;font-size:13px;color:var(--ink);border-bottom:1.5px solid #ccc;padding-bottom:7px}
.qa b{color:var(--red);font-weight:700;margin-right:12px}
.faq-panel{top:91px;left:868px;width:332px;height:123px;background:var(--night);overflow:hidden}
.faq-panel .arc{position:absolute;left:172px;top:-30px;width:180px;height:180px;border-radius:50%;border:16px solid var(--red)}
.faq .btn{position:absolute;top:133px;left:698px;width:294px;height:36px;border-radius:18px;background:var(--red);color:var(--white);font-size:14.5px;font-weight:600;display:flex;align-items:center;justify-content:center}

/* map */
.map{top:2803px;height:272px;background:linear-gradient(160deg,#e6f2e3 0%,#d6ecd6 45%,#eef4e6 100%)}

/* footer */
.footer{top:3075px;height:258px;background:#2a2826;color:#e8e4e0}
.foot-col{position:absolute;top:26px;font-size:9.5px;line-height:1.55}
.foot-col h4{font-size:10px;font-weight:600;letter-spacing:.06em;margin-bottom:8px}
.copy{top:141px;left:0;width:1200px;text-align:center;font-size:9.5px;color:#d0ccc8}
.foot-ghost{top:196px;left:-20px;font-size:80px;font-weight:800;color:rgba(255,255,255,.14);white-space:nowrap;letter-spacing:.02em}
</style>
</head>
<body>

<header class="hero">
  <div class="ph" role="img" aria-label="Evening photo of the open-plan living room with sofas, dining area and glass doors to the garden" style="inset:0;background:linear-gradient(120deg,#2a1f18 0%,#5b4331 45%,#7d5c3d 65%,#2d2621 100%)"></div>
  <div class="hero-shade"></div>
  <div class="abs logo" style="top:38px;left:118px;width:150px;line-height:1.1">CEDAR LANTERN RETREAT</div>
  <nav class="abs nav"><span>The House</span><span>Gallery</span><span>Explore Bend</span><span>Reviews</span><span>Book Direct</span><span>Contact</span><span>FAQ</span></nav>
  <div class="pill light" style="top:36px;left:805px;width:147px">Check Availability</div>
  <div class="pill red" style="top:36px;left:959px;width:122px">Book Direct</div>
  <h1 class="abs hero-title">Cedar Lantern Retreat</h1>
  <div class="abs hero-sub">Bend, Oregon</div>
  <div class="abs facts"><span>3 Bedrooms</span><span>2 Baths</span><span>Sleeps 6</span><span>Pet Friendly</span><span>Walk to Tanager</span></div>
  <div class="pill red" style="top:286px;left:115px;width:147px;height:28px;border-radius:14px">Book Direct &amp; Save</div>
  <div class="pill light" style="top:286px;left:269px;width:147px;height:28px;border-radius:14px">Check Availability</div>
  <div class="abs hero-rule"></div>
  <div class="abs stats"><span><span class="stars">★★★★★</span>&nbsp; 4.98 Rating From 205 Guest Reviews</span><span class="dot"></span><span>Staynest Guest Pick</span><span class="dot"></span><span>Top 1% of Eligible Staynest homes</span><span class="dot"></span><span>Staynest Premier Host, 9 Years Hosting</span></div>
</header>

<section class="intro">
  <div class="ph" role="img" aria-label="Living room with a cream sofa, leather ottoman and wall art" style="left:116px;top:54px;width:207px;height:228px;background:linear-gradient(160deg,#cfc4b6,#a99684 60%,#7f6c5b)"></div>
  <div class="ph" role="img" aria-label="Dining table with wooden chairs set beside the kitchen" style="left:341px;top:54px;width:267px;height:117px;background:linear-gradient(160deg,#e4e1dc,#b7a897 55%,#8a7561)"></div>
  <div class="ph" role="img" aria-label="White console with a plant and decor under a window" style="left:344px;top:189px;width:266px;height:93px;background:linear-gradient(160deg,#f0eeea,#d4ccc2 60%,#a8998a)"></div>
  <h2 class="abs">A Five-minute Walk From The Tanager Quarter, Cedar Lantern Retreat Is Where Central Oregon's Outdoors Meets An Easy, Comfortable Stay.</h2>
  <p class="abs">Freshly Updated With Warm, Thoughtful Furnishings And Ultra-comfortable Beds, The Home Sits On A Quiet Cul-de-sac Just Far Enough From The Action To Feel RESTful — And Close Enough To Walk To Dinner, A Summer Concert At Brightwater Lawn Pavilion, Or The River.</p>
  <div class="abs link" style="top:250px;left:641px">See The Full House</div>
  <div class="abs" style="left:1095px;top:248px;width:180px;height:180px;border-radius:50%;border:38px solid var(--red)"></div>
</section>

<section class="rooms">
  <h2 class="abs">Every Room, Ready for you</h2>
  <p class="abs lede">Three Bedrooms, Two Baths, And The Details That Turn A House Into An Easy Place To Land — A Well-stocked Kitchen, A Fenced Yard, And Parking That Doesn't Require A Plan.</p>

  <div class="card w" style="left:0;top:136px;width:400px;height:146px">
    <svg class="icon" width="40" height="40" viewBox="0 0 40 40" fill="none" stroke="#222" stroke-width="1.6"><rect x="5" y="14" width="30" height="14" rx="2"/><rect x="9" y="17" width="9" height="5" rx="1"/><rect x="22" y="17" width="9" height="5" rx="1"/><path d="M3 28h34v5H3zM6 33v3M34 33v3M12 8l1 2M20 5v3M28 8l-1 2"/></svg>
    <h3>3 Bedrooms, Sleeps 6</h3>
    <p>1 King, 2 Queens — Comfortably Set Up For Families Or Two Couples.</p>
    <div class="arc"></div>
  </div>
  <div class="card p" style="left:400px;top:136px;width:402px;height:146px;background:#fdf6f6">
    <svg class="icon" style="right:285px" width="40" height="46" viewBox="0 0 40 46" fill="none" stroke="#222" stroke-width="1.6"><rect x="3" y="3" width="34" height="40"/><path d="M20 3v40M12 22v4M25 12h8M27 16h1M30 16h1M27 19h1M30 19h1M27 22h1M30 22h1"/></svg>
    <h3 style="left:35px">2 Full Bathrooms</h3>
    <p style="left:38px">Fresh Towels, Good Water Pressure, No Waiting Your Turn.</p>
  </div>
  <div class="card w" style="left:802px;top:136px;width:398px;height:146px">
    <svg class="icon" width="66" height="52" viewBox="0 0 66 52" fill="none" stroke="#222" stroke-width="1.6"><rect x="4" y="20" width="26" height="28"/><rect x="8" y="26" width="18" height="10"/><path d="M10 4h12l4 10H6zM14 14v6M36 24h10v24H36zM50 4h12v44H50zM50 20h12M41 4v20M41 10h4"/></svg>
    <h3 style="left:19px">Well-equipped Kitchen</h3>
    <p style="left:21px">1 King, 2 Queens — Comfortably Set Up For Families Or Two Couples.</p>
  </div>

  <div class="card p" style="left:0;top:282px;width:400px;height:147px">
    <svg class="icon" style="right:auto;left:306px" width="62" height="46" viewBox="0 0 62 46" fill="none" stroke="#222" stroke-width="1.6"><rect x="2" y="2" width="58" height="8"/><rect x="6" y="10" width="50" height="34"/><path d="M18 44V26a13 13 0 0 1 26 0v18M31 38c-5 0-6-5-3-9 1 3 3 2 3 0 4 3 5 9 0 9z"/></svg>
    <h3>Fireplace &amp; Covered Porch</h3>
    <p>Gas Fireplace Inside, Covered Outdoor Seating That Catches The Summer Concerts.</p>
  </div>
  <div class="card w" style="left:400px;top:282px;width:402px;height:147px">
    <svg class="icon" width="96" height="44" viewBox="0 0 96 44" fill="none" stroke="#222" stroke-width="1.6"><path d="M2 14h92M2 30h92M8 42V8l5-6 5 6v34M30 42V8l5-6 5 6v34M52 42V8l5-6 5 6v34M74 42V8l5-6 5 6v34"/></svg>
    <h3 style="left:31px">Fenced Backyard</h3>
    <p style="left:32px;width:290px">Private, secure, and pet-friendly — let the dog out without a second thought.</p>
    <div class="arc"></div>
  </div>
  <div class="card p" style="left:802px;top:282px;width:398px;height:147px">
    <svg class="icon" width="82" height="50" viewBox="0 0 82 50" fill="none" stroke="#222" stroke-width="1.6"><path d="M2 18 41 2l39 16M8 16v32M74 16v32M2 48h78M16 24h50M16 30h50M16 24v24M66 24v24"/><rect x="24" y="34" width="34" height="10" rx="3"/><circle cx="31" cy="44" r="3"/><circle cx="51" cy="44" r="3"/></svg>
    <h3 style="left:13px">Off-Street Driveway Parking</h3>
    <p style="left:15px">Dedicated driveway space — no permits, no street-parking guesswork.</p>
  </div>
</section>

<section class="gallery">
  <div class="abs ghost">WHOLE PROPERTY</div>
  <h2 class="abs">See the Whole Property</h2>
  <div class="ph" role="img" aria-label="Fenced backyard with lawn, rock garden and mature tree" style="left:118px;top:110px;width:480px;height:225px;background:linear-gradient(160deg,#8aa8c8 0%,#7c6a4f 35%,#6a8f3a 70%,#b8b0a0 100%)"></div>
  <div class="ph" role="img" aria-label="Bedroom corner with ladder shelf and window" style="left:606px;top:110px;width:235px;height:109px;background:linear-gradient(160deg,#eeeae4,#cfc6ba)"></div>
  <div class="ph" role="img" aria-label="Front of the house with porch and garden" style="left:848px;top:110px;width:234px;height:109px;background:linear-gradient(160deg,#9fc0e4,#6f8b4e 60%,#b6b2a8)"></div>
  <div class="ph" role="img" aria-label="Bedroom with white bedding opening onto the dining area" style="left:606px;top:225px;width:476px;height:110px;background:linear-gradient(160deg,#f2efea,#ddd3c7 55%,#c4b29c)"></div>
  <div class="ph" role="img" aria-label="Covered patio with fire pit and outdoor seating" style="left:118px;top:343px;width:235px;height:108px;background:linear-gradient(160deg,#5a4b3e,#8a7358 50%,#c9b592)"></div>
  <div class="ph" role="img" aria-label="Bathroom vanity with mirror" style="left:361px;top:343px;width:235px;height:108px;background:linear-gradient(160deg,#e3e6e0,#c6cbbf 60%,#9ca292)"></div>
  <div class="ph" role="img" aria-label="Bathroom with glass shower" style="left:606px;top:343px;width:235px;height:108px;background:linear-gradient(160deg,#e8e8e2,#c2c8ba 60%,#a3a898)"></div>
  <div class="ph" role="img" aria-label="Bathroom with green walls and tub" style="left:848px;top:343px;width:234px;height:108px;background:linear-gradient(160deg,#dfe6df,#a9bcaa 55%,#e9ebe7)"></div>
  <div class="abs link">VIEW FULL GALLERY</div>
</section>

<section class="reviews">
  <h2 class="abs">What <em>205</em> Guests are Saying</h2>
  <div class="abs score">4.98</div>
  <div class="abs score-stars">★★★★★</div>
  <div class="abs score-note">205 Verified Staynest Reviews</div>
  <div class="metric" style="left:377px;top:118px">Cleanliness — <b>5.0</b></div>
  <div class="metric" style="left:610px;top:118px">Accuracy — <b>5.0</b></div>
  <div class="metric" style="left:838px;top:118px">Check-in — <b>5.0</b></div>
  <div class="metric" style="left:377px;top:162px">Communication — <b>5.0</b></div>
  <div class="metric" style="left:610px;top:162px">Location — <b>5.0</b></div>
  <div class="metric" style="left:838px;top:162px">Value — <b>4.8</b></div>
  <div class="chip" style="left:124px;width:217px">Hospitality · <b>Mentioned 118×</b></div>
  <div class="chip" style="left:351px;width:148px">Walkability · <b>44×</b></div>
  <div class="chip" style="left:511px;width:148px">Comfort · <b>47×</b></div>
  <div class="chip" style="left:673px;width:148px">Backyard · <b>34×</b></div>
  <div class="chip" style="left:829px;width:148px">Backyard · <b>41×</b></div>
  <div class="quote" style="left:130px;top:305px;width:275px">"Walked to dinner, walked to the concert, walked back. Didn't move the car once."<cite>Dana Whitlock</cite></div>
  <div class="quote-card"></div>
  <div class="quote" style="left:468px;top:305px;width:285px">"Spotless, exactly as pictured, and the backyard was perfect for our dog."<cite style="margin-top:26px">Priya L.</cite></div>
  <div class="quote" style="left:804px;top:305px;width:285px">"Ruth responded in minutes. Easiest check-in we've had anywhere."<cite style="margin-top:26px">Marcus T.</cite></div>
</section>

<section class="direct">
  <div class="ph" role="img" aria-label="Guest sitting on the floor booking on a laptop in a bright room" style="inset:0;border-radius:0;background:linear-gradient(135deg,#6e5e50 0%,#a89584 40%,#d4c4b0 70%,#8a7563 100%)"></div>
  <div class="abs direct-card">
    <h2>Book Direct, Stay The<br>Same Trusted Way</h2>
    <p class="lede">Same House, Same Hospitality, Same Calendar As Staynest and Lodgr — Just Without The Extra Service Fee.</p>
    <div class="step" style="top:128px"><svg width="24" height="22" viewBox="0 0 24 22" fill="none" stroke="#fff" stroke-width="1.5"><rect x="2" y="3" width="20" height="17" rx="1"/><path d="M2 8h20M7 1v4M17 1v4M6 12h2M11 12h2M16 12h2M6 16h2M11 16h2"/></svg>Pick your Dates</div>
    <div class="step" style="top:159px"><svg width="24" height="24" viewBox="0 0 24 24" fill="none" stroke="#fff" stroke-width="1.5"><circle cx="12" cy="12" r="10"/><circle cx="12" cy="12" r="6.5"/><path d="M13.8 9.6c-.5-.8-3.6-1-3.6.7s3.6.9 3.6 2.8-3 1.6-3.7.6M12 7.8v8.4"/></svg>See The Full Price Upfront</div>
    <div class="step" style="top:188px"><svg width="26" height="24" viewBox="0 0 26 24" fill="none" stroke="#fff" stroke-width="1.5"><rect x="8" y="2" width="16" height="11" rx="1"/><path d="M8 6h16M1 16l5-3h5l3 2h-5M1 22l5-2h7l8-5"/></svg>Pay Securely, Confirm Instantly</div>
    <div class="btn">Book Now</div>
    <div class="arc"></div>
  </div>
</section>

<section class="faq">
  <h2 class="abs">Questions Before you Book?</h2>
  <div class="qa" style="top:112px"><b>Q:</b>Are Pets allowed?</div>
  <div class="qa" style="top:141px"><b>Q:</b>Where do we park?</div>
  <div class="qa" style="top:169px"><b>Q:</b>What are check-in / check-out times?</div>
  <div class="qa" style="top:198px;border-bottom:none"><b>Q:</b>What's the cancellation Policy?</div>
  <div class="abs faq-panel"><div class="arc"></div></div>
  <div class="btn">Send Message Now</div>
</section>

<section class="map">
  <div class="ph" role="img" aria-label="Road map of the surrounding region showing the property location" style="inset:0;border-radius:0;background:linear-gradient(160deg,#e8f1e2 0%,#d3e9d3 45%,#eef2e4 100%)"></div>
  <svg class="abs" style="left:648px;top:110px" width="70" height="64" viewBox="0 0 70 64"><ellipse cx="35" cy="54" rx="33" ry="9" fill="var(--red)"/><ellipse cx="35" cy="54" rx="22" ry="5" fill="#f3e3df"/><path d="M35 56C22 40 14 32 14 21a21 21 0 0 1 42 0c0 11-8 19-21 35z" fill="var(--red)"/><circle cx="35" cy="21" r="8" fill="#fff"/></svg>
</section>

<footer class="footer">
  <div class="abs logo" style="top:56px;left:158px;width:150px;font-size:15px;line-height:1.1">CEDAR LANTERN RETREAT</div>
  <div class="abs" style="top:103px;left:225px;width:18px;height:18px;border-radius:50%;border:1.5px solid #e8e4e0"></div>
  <div class="foot-col" style="left:432px"><h4>QUICK LINKS</h4>The House<br>Photo Gallery<br>Explore Bend<br>Guest Reviews</div>
  <div class="foot-col" style="left:572px"><h4>BOOK</h4>Check Availability<br>Book Direct<br>Contact / FAQ</div>
  <div class="foot-col" style="left:733px"><h4>ALSO LISTED ON</h4>Staynest listing ↗<br>Lodgr listing ↗</div>
  <div class="foot-col" style="left:935px"><h4>CONTACT US</h4></div>
  <svg class="abs" style="left:887px;top:72px" width="24" height="24" viewBox="0 0 24 24" fill="none" stroke="#e8e4e0" stroke-width="1.4"><circle cx="12" cy="12" r="11"/><rect x="6" y="8" width="12" height="8" rx="1"/><path d="m6 8 6 5 6-5"/></svg>
  <div class="abs" style="top:77px;left:932px;font-size:11px;text-decoration:underline">info@cedarlantern.example</div>
  <div class="abs copy">© 2026 Cedar Lantern Retreat . All rights reserved. &nbsp;|&nbsp; Privacy Policy &nbsp;&nbsp;|&nbsp; Terms and Conditions</div>
  <div class="abs foot-ghost">CEDAR LANTERN RETREAT</div>
</footer>

</body>
</html>
```